Accounting firm needing business card / letterhead designed
Marcus L. Tembrook, CPA
marcus@lumenfiledesk.com
www.lumenfiledesk.com
482 E Larkin Ave Brookfield, WI 53045
262-555-0172
Business

```html
<!DOCTYPE html>
<html lang="en">
<head>
<meta charset="utf-8">
<title>Lumen File Desk – Business Card</title>
<link rel="stylesheet" href="https://fonts.googleapis.com/css2?family=Montserrat:wght@500;600;700&family=Mulish:wght@400;500&display=swap">
<style>
  :root {
    --backdrop: #2a2a2a;
    --card: #1f1f1f;
    --card-edge: #2c2c2c;
    --indigo: #3b3494;
    --lime: #7cc13a;
    --ink: #f2f2f2;
    --silver: #8f8f8f;
  }
  * { margin: 0; padding: 0; box-sizing: border-box; }
  html, body { width: 1200px; height: 900px; overflow: hidden; }
  body {
    background: var(--backdrop);
    font-family: "Mulish", "Helvetica Neue", Arial, sans-serif;
    color: var(--ink);
    position: relative;
  }
  .card {
    position: absolute;
    left: 250px;
    width: 700px;
    height: 400px;
    background: var(--card);
    border: 1px solid var(--card-edge);
    box-shadow: 0 14px 30px rgba(0,0,0,.45);
  }
  .card--back { top: 35px; }
  .card--front { top: 465px; }

  /* back side */
  .back-wordmark {
    position: absolute;
    top: 150px; left: 0; right: 0;
    text-align: center;
    font-family: "Montserrat", Arial, sans-serif;
    font-weight: 600;
    font-size: 40px;
    letter-spacing: 6px;
    color: var(--silver);
  }
  .back-url {
    position: absolute;
    bottom: 34px; left: 0; right: 0;
    text-align: center;
    font-size: 17px;
    letter-spacing: 1px;
  }
  .url-domain { color: var(--lime); }

  /* front side */
  .front-wordmark {
    position: absolute;
    top: 160px; left: 30px;
    width: 330px;
    white-space: nowrap;
    font-family: "Montserrat", Arial, sans-serif;
    font-weight: 600;
    font-size: 26px;
    letter-spacing: 2px;
    color: var(--indigo);
  }
  .divider {
    position: absolute;
    left: 370px; top: 115px;
    width: 3px; height: 130px;
    background: var(--lime);
  }
  .contact {
    position: absolute;
    left: 395px; top: 110px;
  }
  .contact__name {
    font-family: "Montserrat", Arial, sans-serif;
    font-weight: 700;
    font-size: 22px;
    color: var(--lime);
    text-transform: uppercase;
  }
  .contact__title {
    font-family: "Montserrat", Arial, sans-serif;
    font-weight: 500;
    font-size: 17px;
    margin-bottom: 14px;
  }
  .contact__row {
    display: flex;
    align-items: center;
    gap: 12px;
    font-size: 17px;
    letter-spacing: .5px;
    margin-bottom: 6px;
  }
  .contact__row svg { width: 18px; height: 18px; flex: none; }
  .address {
    position: absolute;
    bottom: 40px; left: 0; right: 0;
    text-align: center;
    font-size: 19px;
    letter-spacing: .5px;
  }
</style>
</head>
<body>
  <section class="card card--back">
    <div class="back-wordmark">LUMEN FILE DESK</div>
    <div class="back-url">www.<span class="url-domain">lumenfiledesk</span>.com</div>
  </section>

  <section class="card card--front">
    <div class="front-wordmark">LUMEN FILE DESK</div>
    <div class="divider"></div>
    <div class="contact">
      <div class="contact__name">Marcus L. Tembrook</div>
      <div class="contact__title">CPA</div>
      <div class="contact__row">
        <svg viewBox="0 0 18 18" aria-hidden="true"><rect x="5" y="1.5" width="8" height="15" rx="1.5" fill="none" stroke="#7cc13a" stroke-width="1.6"/><line x1="8" y1="14" x2="10" y2="14" stroke="#7cc13a" stroke-width="1.4"/></svg>
        <span>262-555-0172</span>
      </div>
      <div class="contact__row">
        <svg viewBox="0 0 18 18" aria-hidden="true"><rect x="1.5" y="4" width="15" height="10" fill="#7cc13a"/><polyline points="1.5,4 9,10 16.5,4" fill="none" stroke="#1f1f1f" stroke-width="1.4"/></svg>
        <span>marcus@lumenfiledesk.com</span>
      </div>
      <div class="contact__row">
        <svg viewBox="0 0 18 18" aria-hidden="true"><g fill="none" stroke="#7cc13a" stroke-width="1.4"><circle cx="9" cy="9" r="7.2"/><ellipse cx="9" cy="9" rx="3.2" ry="7.2"/><line x1="1.8" y1="9" x2="16.2" y2="9"/><line x1="9" y1="1.8" x2="9" y2="16.2"/></g></svg>
        <span>www.<span class="url-domain">lumenfiledesk</span>.com</span>
      </div>
    </div>
    <div class="address">482 E Larkin Ave Brookfield, WI 53045</div>
  </section>
</body>
</html>
```